Packaging label for spirit line

We currently have a various line of spirits and are looking to rebrand the label. The bottle would stay the same since there is a lot of stock. An example of the current situation has been attached. The entire collection is to be found on our website: www.velvetparlor.quinmark.be/spirits

These spirits are a product created by our cocktail bar "Velvet Parlor". The name however, would likely change to "Tipplefox" or plural "Tipplefoxes" since we'd like to split those 2 businesses. The series "shaker lineup" would remain the same as it is a complete series mainly invented for mixology.

The current label is fine, but needs that extra spark that makes it stand out on a shelve compared to other spirit bottles. We envision a more funky yet sophisticated branding with perhaps goldtrims for that "exclusive, luxurious" feel and very much like a vintage animal humification vibe (for example: the marigold or fennick's). Preferably a french bulldog as this has been our mascotte since the very beginning of starting this business.

Last but not least, the measurements: max. 90 mm height and max. 260 mm length. The current label is 90x180mm. 260mm means the label goes fully around the bottle.

Industry/Entity Type

Alcoholic Beverages

Font styles to use
Serif
Sans Serif

Requirements
Must have
• The label must have the standard information such as the product name, the alcohol %, the volume ml and room for ean code. The bottle needs to be sealed for shipment, so a little seal to cover the lid is required.
Nice to have
• It would be nice to maintain consistency with for example the same animal but change of background / colors / outfit / etc to clarify the different flavors. A cutout/contour is also preferable for added interest, so that the label is not square.
Should not have
• The label should definitely not be childish or too much. The overal look and feel needs to be professional yet not too serious.

```html
<!DOCTYPE html>
<html lang="en">
<head>
<meta charset="utf-8">
<title>Tipplefoxes London Dry Gin – Label</title>
<link rel="stylesheet" href="https://fonts.googleapis.com/css2?family=Josefin+Sans:wght@700&family=Oswald:wght@500&family=Roboto+Slab:wght@400;500&display=swap">
<style>
  :root {
    --backdrop: #ececec;
    --paper: #efefed;
    --paper-edge: #dcdcda;
    --lagoon: #1bbfd0;
    --copper: #c0773f;
    --copper-soft: #d9a27a;
    --ink: #1d1f22;
    --brand-silver: #e6e6e4;
    --art-light: #d9d9d7;
    --art-dark: #8d8d8b;
  }
  html, body {
    margin: 0;
    width: 1200px;
    height: 1091px;
    overflow: hidden;
    background: var(--backdrop);
  }
  .label-sheet {
    display: block;
    width: 1200px;
    height: 1091px;
  }
  .seal-strip { fill: var(--paper); stroke: var(--paper-edge); stroke-width: 1; }
  .trim-area { fill: var(--copper-soft); opacity: .85; }
  .panel { fill: var(--paper); }
  .band { fill: var(--lagoon); }
  .copper-line { fill: none; stroke: var(--copper); stroke-width: 1.6; }
  .rule { stroke: var(--ink); stroke-width: 1; opacity: .7; }
  .arc-title {
    font-family: "Roboto Slab", serif;
    font-size: 17px;
    letter-spacing: 6px;
    fill: var(--copper);
  }
  .origin {
    font-family: "Roboto Slab", serif;
    font-weight: 500;
    font-size: 13px;
    letter-spacing: 3px;
    fill: var(--copper);
  }
  .brand-name {
    font-family: "Josefin Sans", sans-serif;
    font-weight: 700;
    font-size: 48px;
    letter-spacing: 3px;
    fill: var(--brand-silver);
  }
  .product-name {
    font-family: "Oswald", sans-serif;
    font-weight: 500;
    font-size: 27px;
    letter-spacing: 11px;
    fill: var(--ink);
  }
  .spec {
    font-family: "Roboto Slab", serif;
    font-size: 21px;
    fill: var(--ink);
  }
  .spec-small {
    font-family: "Oswald", sans-serif;
    font-weight: 500;
    font-size: 16px;
    fill: var(--ink);
  }
  .distiller {
    font-family: "Roboto Slab", serif;
    font-size: 13px;
    letter-spacing: 1.5px;
    fill: var(--ink);
  }
  .stamp { fill: none; stroke: var(--copper); stroke-width: 2; }
</style>
</head>
<body>
<svg class="label-sheet" viewBox="0 0 1200 1091" xmlns="http://www.w3.org/2000/svg">
  <defs>
    <linearGradient id="mascotTone" x1="0" y1="0" x2="0" y2="1">
      <stop offset="0" stop-color="var(--art-light)"/>
      <stop offset="1" stop-color="var(--art-dark)"/>
    </linearGradient>
    <path id="titleArc" d="M470,318 Q600,282 730,318"/>
  </defs>

  <g class="neck-seal">
    <rect class="seal-strip" x="575" y="30" width="50" height="170"/>
    <rect class="trim-area" x="576" y="162" width="48" height="24"
          role="img" aria-label="Copper foil trim pattern on the seal"/>
  </g>

  <path class="band" d="M210,750 L225,742 L240,750 L255,742 L270,750 L285,742 L300,750 L315,742 L330,750 L345,742 L360,750
    L840,750 L855,742 L870,750 L885,742 L900,750 L915,742 L930,750 L945,742 L960,750 L975,742 L990,750
    L990,1040 L210,1040 Z"/>

  <path class="panel" d="M340,330 Q340,255 420,252 L780,252 Q860,255 860,330 L860,750 L815,800 L385,800 L340,750 Z"/>
  <path class="copper-line" d="M362,350 L362,330 Q362,278 428,276 M772,276 Q838,278 838,330 L838,350"/>
  <line class="copper-line" x1="362" y1="300" x2="362" y2="735"/>
  <line class="copper-line" x1="838" y1="300" x2="838" y2="735"/>
  <line class="copper-line" x1="362" y1="735" x2="400" y2="778"/>
  <line class="copper-line" x1="838" y1="735" x2="800" y2="778"/>

  <text class="arc-title"><textPath href="#titleArc" startOffset="50%" text-anchor="middle">DISTILLED SPIRITS</textPath></text>

  <rect class="mascot-art" x="440" y="330" width="320" height="400" rx="6" fill="url(#mascotTone)"
        role="img" aria-label="Vintage engraving of a French bulldog in a top hat and tailcoat with copper trims"/>

  <text class="origin" x="600" y="788" text-anchor="middle">PRODUCT OF BELGIUM</text>

  <text class="brand-name" x="600" y="868" text-anchor="middle">TIPPLEFOXES</text>
  <text class="product-name" x="600" y="914" text-anchor="middle">LONDON DRY GIN</text>

  <line class="rule" x1="420" y1="934" x2="800" y2="934"/>
  <text class="spec" x="470" y="962" text-anchor="middle">700 ML</text>
  <line class="rule" x1="522" y1="944" x2="522" y2="970"/>
  <text class="spec" x="583" y="962" text-anchor="middle">38% VOL</text>
  <line class="rule" x1="643" y1="944" x2="643" y2="970"/>
  <text class="spec-small" x="690" y="961" text-anchor="middle">BATCH NO</text>
  <line class="rule" x1="420" y1="976" x2="800" y2="976"/>
  <text class="distiller" x="610" y="997" text-anchor="middle">DISTILLED BY QUINMARK ENTERPRISE BV</text>
  <line class="rule" x1="420" y1="1006" x2="800" y2="1006"/>

  <circle class="stamp" cx="895" cy="935" r="52"/>

  <rect class="trim-area" x="210" y="1014" width="780" height="20"
        role="img" aria-label="Copper foil trim pattern along the label's lower edge"/>
</svg>
</body>
</html>
```